Powerpoint contest

We need to re-design our powerpoints to be much more consistent. All the details are mentioned here. I have more than 30 slides to be created in all.

https://www.pagevault.example/gravik/All-Powerpoints-3c7e91d2ab0f4e6c8d15b27a90e4cf61

Requirements
Must have
• Colors should be greyscale and bravocell pink (ea0a8e) used in small amounts just for accents.

```html
<!DOCTYPE html>
<html lang="en">
<head>
<meta charset="utf-8">
<title>Gravik Presentation Slide System</title>
<link rel="stylesheet" href="https://fonts.googleapis.com/css2?family=Montserrat:wght@400;500;600;700;800&display=swap">
<style>
:root{
  --pink:#ea0a8e;
  --pink-soft:#fbd3ea;
  --ink:#2e2e2e;
  --charcoal:#3a3a3a;
  --grey:#7d7d7d;
  --grey-mid:#bdbdbd;
  --grey-light:#dedede;
  --grey-pale:#f3f3f3;
  --bg:#e4e4e4;
  --white:#fff;
}
*{box-sizing:border-box;margin:0;padding:0}
html,body{width:783px;height:1200px;overflow:hidden}
body{background:var(--bg);font-family:'Montserrat',sans-serif;color:var(--ink);position:relative}
.slide{position:absolute;background:var(--white);overflow:hidden;box-shadow:0 1px 3px rgba(0,0,0,.18)}
.slide.dark{background:var(--charcoal);color:var(--white)}
.brand{position:absolute;display:flex;align-items:center;gap:3px;font-weight:700;font-size:7px;color:var(--ink)}
.brand::before{content:"";width:5px;height:5px;background:var(--pink)}
.dark .brand{color:var(--white)}
.slide-title{position:absolute;left:12px;top:9px;font-weight:800;color:var(--ink);font-size:7px;letter-spacing:.2px;text-transform:uppercase;line-height:1.3}
.slide-title::after{content:"";display:block;width:16px;height:2px;background:var(--pink);margin-top:3px}
.photo{position:absolute;background:linear-gradient(135deg,#8f8f8f,#c9c9c9 60%,#e2e2e2)}
.footer{position:absolute;left:0;right:0;bottom:0;height:10px;background:var(--grey-pale)}
.footer .brand{left:8px;top:2px;font-size:5px}
.footer .brand::before{width:4px;height:4px}
.footer .num{position:absolute;right:8px;top:2.5px;font-size:4.5px;color:var(--grey)}
.box{position:absolute;font-size:5px;font-weight:600;display:flex;align-items:center;justify-content:center;text-align:center;line-height:1.25;padding:2px}
.note{position:absolute;font-size:4.5px;line-height:1.45;color:var(--grey)}
.note b{display:block;color:var(--ink);font-size:5px;font-weight:700}
.bullets{position:absolute;font-size:5px;line-height:2;color:var(--ink);list-style:none}
.bullets li::before{content:"";display:inline-block;width:3px;height:3px;background:var(--pink);margin-right:4px;vertical-align:1px}

/* intro */
.intro{background:var(--charcoal);color:var(--white)}
.intro h1{position:absolute;font-weight:800}
.intro p{position:absolute;line-height:1.35;color:#e6e6e6}
.intro .photo{top:0;right:0;bottom:0;width:44%}
.intro .fade{position:absolute;top:0;bottom:0;right:34%;width:14%;background:linear-gradient(90deg,var(--charcoal),rgba(58,58,58,0))}
.intro .accent{position:absolute;height:3px;background:var(--pink)}
table.grid{position:absolute;border-collapse:collapse;font-size:4.5px}
table.grid th{background:var(--grey-light);font-weight:700;padding:2px 3px;text-align:left}
table.grid td{border:.5px solid var(--grey-light);padding:2px 3px;height:11px;color:var(--grey)}
table.grid td.on{text-align:center}
table.grid td.on::before{content:"";display:inline-block;width:4px;height:4px;border-radius:50%;background:var(--pink)}
</style>
</head>
<body>

<!-- Hero intro slide -->
<section class="slide intro" style="left:248px;top:30px;width:288px;height:162px">
  <div class="photo" role="img" aria-label="Photo of business people in an office"></div>
  <div class="fade"></div>
  <div class="accent" style="left:18px;top:34px;width:22px"></div>
  <h1 style="left:18px;top:40px;font-size:24px">Introduction</h1>
  <p style="left:18px;top:74px;width:150px;font-size:7px">A clear look at how our release platform keeps teams in sync.</p>
  <p style="left:18px;top:100px;font-size:5px;color:var(--grey-mid)">June 2024</p>
  <div class="brand" style="left:18px;bottom:14px;font-size:9px">Gravik</div>
</section>

<!-- Intro variants -->
<section class="slide intro" style="left:232px;top:250px;width:157px;height:88px">
  <div class="accent" style="left:10px;top:15px;width:14px;height:2px"></div>
  <h1 style="left:10px;top:18px;font-size:14px">Introduction</h1>
  <p style="left:10px;top:38px;width:110px;font-size:4.5px">A clear look at how our release platform keeps teams in sync.</p>
  <p style="left:10px;top:54px;font-size:4px;color:var(--grey-mid)">June 2024</p>
  <div class="brand" style="left:10px;bottom:8px;font-size:6px">Gravik</div>
</section>
<section class="slide intro" style="left:396px;top:250px;width:157px;height:88px">
  <div class="photo" role="img" aria-label="Photo of business people in an office"></div>
  <div class="fade"></div>
  <div class="accent" style="left:10px;top:15px;width:14px;height:2px"></div>
  <h1 style="left:10px;top:18px;font-size:14px">Introduction</h1>
  <p style="left:10px;top:38px;width:78px;font-size:4.5px">A clear look at how our release platform keeps teams in sync.</p>
  <p style="left:10px;top:62px;font-size:4px;color:var(--grey-mid)">June 2024</p>
</section>

<!-- Row 1 -->
<section class="slide" style="left:31px;top:395px;width:232px;height:130px">
  <div class="brand" style="left:12px;top:14px">Gravik</div>
  <div style="position:absolute;left:12px;top:50px;font-weight:800;font-size:10px;text-transform:uppercase">Gravik <span style="color:var(--pink)">Presentation</span></div>
  <div style="position:absolute;left:12px;top:65px;font-size:5px;color:var(--grey)">Company overview deck</div>
  <div style="position:absolute;left:0;right:0;bottom:0;height:26px;background:var(--grey-pale)"></div>
  <div style="position:absolute;left:12px;bottom:10px;font-size:4.5px;color:var(--grey)">June 2024 · Internal use</div>
</section>
<section class="slide dark" style="left:275px;top:395px;width:232px;height:130px">
  <svg width="232" height="130" style="position:absolute;left:0;top:0"><path d="M232 0 L232 130 L150 130 Q200 70 232 0Z" fill="#2a2a2a"/><path d="M150 130 Q200 70 232 0" fill="none" stroke="var(--pink)" stroke-width="1.5"/></svg>
  <div style="position:absolute;left:14px;top:48px;font-weight:800;font-size:10px;text-transform:uppercase">Gravik Presentation</div>
  <div style="position:absolute;left:14px;top:62px;width:18px;height:2px;background:var(--pink)"></div>
  <div style="position:absolute;left:14px;top:68px;font-size:5px;color:#dcdcdc">Platform overview</div>
  <div class="brand" style="left:14px;bottom:12px">Gravik</div>
</section>
<section class="slide" style="left:519px;top:395px;width:232px;height:130px">
  <div class="photo" style="left:0;top:0;width:110px;height:120px" role="img" aria-label="Photo of a team meeting"></div>
  <div class="slide-title" style="left:120px;top:14px">Company Profile</div>
  <ul class="bullets" style="left:120px;top:32px">
    <li>Founded to simplify releases</li>
    <li>Teams across four regions</li>
    <li>Built for secure delivery</li>
    <li>Trusted by global brands</li>
  </ul>
  <div class="footer"><div class="brand">Gravik</div><span class="num">03</span></div>
</section>

<!-- Row 2 -->
<section class="slide" style="left:31px;top:555px;width:232px;height:130px">
  <div class="slide-title">Release Comparison</div>
  <table class="grid" style="left:12px;top:26px;width:208px">
    <tr><th>Capability</th><th>Manual</th><th>Scripts</th><th>Gravik</th></tr>
    <tr><td>Version control</td><td class="on"></td><td class="on"></td><td class="on"></td></tr>
    <tr><td>Rollback</td><td></td><td class="on"></td><td class="on"></td></tr>
    <tr><td>Audit trail</td><td></td><td></td><td class="on"></td></tr>
    <tr><td>Merge checks</td><td></td><td class="on"></td><td class="on"></td></tr>
    <tr><td>Compliance</td><td></td><td></td><td class="on"></td></tr>
  </table>
  <div class="footer"><div class="brand">Gravik</div><span class="num">04</span></div>
</section>
<section class="slide" style="left:275px;top:555px;width:232px;height:130px">
  <div class="slide-title">Program Release Lifecycle</div>
  <div class="box" style="left:12px;top:28px;width:208px;height:12px;background:var(--charcoal);color:#fff">Plan</div>
  <div class="box" style="left:12px;top:44px;width:100px;height:20px;background:var(--grey-light)">Build</div>
  <div class="box" style="left:120px;top:44px;width:100px;height:20px;background:var(--grey-light)">Test</div>
  <div class="box" style="left:12px;top:68px;width:208px;height:12px;background:var(--grey-pale);border-left:3px solid var(--pink)">Ship</div>
  <div class="note" style="left:12px;top:86px;width:208px">Every release follows the same four stages, with review gates between each one.</div>
  <div class="footer"><div class="brand">Gravik</div><span class="num">05</span></div>
</section>
<section class="slide" style="left:519px;top:555px;width:232px;height:130px">
  <div class="slide-title" style="width:150px">Working Central Platform for the Enterprise</div>
  <div class="box" style="left:12px;top:38px;width:60px;height:22px;background:var(--grey-pale)">Source control</div>
  <div class="box" style="left:78px;top:38px;width:60px;height:22px;background:var(--charcoal);color:#fff;border-bottom:2px solid var(--pink)">Gravik core</div>
  <div class="box" style="left:12px;top:64px;width:126px;height:20px;background:var(--grey-pale)">Automated testing and review</div>
  <div class="box" style="left:12px;top:88px;width:126px;height:14px;background:var(--grey-light)">Secure deployment</div>
  <div class="box" style="left:160px;top:36px;width:60px;height:13px;background:var(--grey-pale)">Sales teams</div>
  <div class="box" style="left:160px;top:53px;width:60px;height:13px;background:var(--grey-pale)">Service teams</div>
  <div class="box" style="left:160px;top:70px;width:60px;height:13px;background:var(--grey-pale)">Admins</div>
  <div class="box" style="left:160px;top:87px;width:60px;height:13px;background:var(--grey-pale)">Developers</div>
  <div class="footer"><div class="brand">Gravik</div><span class="num">06</span></div>
</section>

<!-- Row 3 -->
<section class="slide" style="left:31px;top:715px;width:232px;height:130px">
  <div class="slide-title">Customer Solutions</div>
  <div style="position:absolute;left:12px;top:26px;width:70px;height:88px;background:var(--charcoal);color:#fff;padding:8px 6px;border-top:3px solid var(--pink)">
    <div style="font-weight:800;font-size:8px;line-height:1.1">Our Approach</div>
    <div style="font-size:4.5px;margin-top:6px;line-height:1.4;color:#ddd">One secure path from sandbox to production.</div>
  </div>
  <div class="note" style="left:90px;top:26px;width:130px;height:26px;background:var(--grey-pale);padding:4px 6px"><b>Faster releases</b>Ship changes in hours, not weeks.</div>
  <div class="note" style="left:90px;top:57px;width:130px;height:26px;background:var(--grey-pale);padding:4px 6px"><b>Fewer errors</b>Automated checks catch conflicts early.</div>
  <div class="note" style="left:90px;top:88px;width:130px;height:26px;background:var(--grey-pale);padding:4px 6px"><b>Full visibility</b>Every change is tracked and auditable.</div>
  <div class="footer"><div class="brand">Gravik</div><span class="num">07</span></div>
</section>
<section class="slide" style="left:275px;top:715px;width:232px;height:130px">
  <div class="slide-title">Customer Success</div>
  <svg width="90" height="90" viewBox="0 0 90 90" style="position:absolute;left:71px;top:24px">
    <circle cx="45" cy="45" r="32" fill="none" stroke="var(--grey-light)" stroke-width="14"/>
    <circle cx="45" cy="45" r="32" fill="none" stroke="var(--pink)" stroke-width="14" stroke-dasharray="197 4" transform="rotate(-90 45 45)"/>
    <text x="45" y="48" text-anchor="middle" font-family="Montserrat,sans-serif" font-weight="800" font-size="10" fill="var(--ink)">98%</text>
  </svg>
  <div class="note" style="left:12px;top:36px;width:55px"><b>Adoption</b>Teams live within 30 days.</div>
  <div class="note" style="left:12px;top:70px;width:55px"><b>Retention</b>Customers renew year on year.</div>
  <div class="note" style="left:168px;top:36px;width:55px"><b>Support</b>Help on hand around the clock.</div>
  <div class="note" style="left:168px;top:70px;width:55px"><b>Satisfaction</b>Rated highly by admins.</div>
  <div class="footer"><div class="brand">Gravik</div><span class="num">08</span></div>
</section>
<section class="slide" style="left:519px;top:715px;width:232px;height:130px">
  <div class="slide-title">Current Customers</div>
  <div style="position:absolute;left:12px;top:28px;display:grid;grid-template-columns:repeat(5,36px);gap:6px">
    <span style="height:14px;background:var(--grey-light)"></span><span style="height:14px;background:var(--grey-light)"></span><span style="height:14px;background:var(--grey-light)"></span><span style="height:14px;background:var(--grey-light)"></span><span style="height:14px;background:var(--grey-light)"></span>
    <span style="height:14px;background:var(--grey-light)"></span><span style="height:14px;background:var(--grey-light)"></span><span style="height:14px;background:var(--grey-light)"></span><span style="height:14px;background:var(--grey-light)"></span><span style="height:14px;background:var(--grey-light)"></span>
    <span style="height:14px;background:var(--grey-light)"></span><span style="height:14px;background:var(--grey-light)"></span><span style="height:14px;background:var(--grey-light)"></span><span style="height:14px;background:var(--grey-light)"></span><span style="height:14px;background:var(--grey-light)"></span>
  </div>
  <div class="note" style="left:12px;top:92px;width:208px">Trusted by enterprise teams in retail, finance, health and telecom.</div>
  <div class="footer"><div class="brand">Gravik</div><span class="num">09</span></div>
</section>

<!-- Row 4 -->
<section class="slide" style="left:31px;top:875px;width:232px;height:130px">
  <div class="slide-title">Application Development Flow</div>
  <svg width="208" height="40" style="position:absolute;left:12px;top:44px">
    <g fill="var(--charcoal)"><rect x="0" y="8" width="38" height="22"/><rect x="56" y="8" width="38" height="22"/><rect x="112" y="8" width="38" height="22"/></g>
    <rect x="168" y="8" width="38" height="22" fill="var(--pink)"/>
    <g stroke="var(--grey)" stroke-width="1.2" fill="var(--grey)"><path d="M40 19H52"/><path d="M52 16L55 19L52 22Z"/><path d="M96 19H108"/><path d="M108 16L111 19L108 22Z"/><path d="M152 19H164"/><path d="M164 16L167 19L164 22Z"/></g>
    <g font-family="Montserrat,sans-serif" font-size="5" font-weight="700" fill="#fff" text-anchor="middle"><text x="19" y="21">Idea</text><text x="75" y="21">Code</text><text x="131" y="21">Review</text><text x="187" y="21">Deploy</text></g>
  </svg>
  <div class="note" style="left:12px;top:88px;width:208px">Each change moves through review before it reaches production.</div>
  <div class="footer"><div class="brand">Gravik</div><span class="num">10</span></div>
</section>
<section class="slide" style="left:275px;top:875px;width:232px;height:130px">
  <div class="slide-title">Sea of Development</div>
  <div class="box" style="left:60px;top:30px;width:112px;height:15px;background:var(--grey-light)">Shared sandbox</div>
  <div class="box" style="left:44px;top:49px;width:144px;height:15px;background:var(--grey-light)">Parallel builds</div>
  <div class="box" style="left:28px;top:68px;width:176px;height:15px;background:var(--charcoal);color:#fff;border-bottom:2px solid var(--pink)">Merge</div>
  <div class="box" style="left:12px;top:87px;width:208px;height:15px;background:var(--grey-pale)">Production release</div>
  <div class="footer"><div class="brand">Gravik</div><span class="num">11</span></div>
</section>
<section class="slide" style="left:519px;top:875px;width:232px;height:130px">
  <div class="slide-title">Maturity Model</div>
  <svg width="208" height="86" style="position:absolute;left:12px;top:26px">
    <g fill="var(--grey-mid)"><rect x="10" y="56" width="28" height="20"/><rect x="50" y="46" width="28" height="30"/><rect x="90" y="34" width="28" height="42"/><rect x="130" y="20" width="28" height="56"/></g>
    <rect x="170" y="4" width="28" height="72" fill="var(--pink)"/>
    <path d="M0 76.5H208" stroke="var(--grey-light)"/>
    <g font-family="Montserrat,sans-serif" font-size="4.5" fill="var(--grey)" text-anchor="middle"><text x="24" y="84">Manual</text><text x="64" y="84">Scripted</text><text x="104" y="84">Managed</text><text x="144" y="84">Automated</text><text x="184" y="84">Optimised</text></g>
  </svg>
  <div class="footer"><div class="brand">Gravik</div><span class="num">12</span></div>
</section>

<!-- Row 5 -->
<section class="slide dark" style="left:31px;top:1035px;width:232px;height:130px">
  <div style="position:absolute;left:14px;top:50px;font-weight:800;font-size:10px;line-height:1.15;text-transform:uppercase">Current<br>State</div>
  <div style="position:absolute;left:14px;top:76px;width:18px;height:2px;background:var(--pink)"></div>
  <svg width="110" height="110" viewBox="-55 -55 110 110" style="position:absolute;left:110px;top:10px">
    <g fill="none" stroke="rgba(255,255,255,.4)" stroke-width=".8">
      <polygon points="0,-45 43,-14 27,36 -27,36 -43,-14"/>
      <polygon points="0,-30 29,-9 18,24 -18,24 -29,-9"/>
      <polygon points="0,-15 14,-5 9,12 -9,12 -14,-5"/>
      <path d="M0 0L0 -45M0 0L43 -14M0 0L27 36M0 0L-27 36M0 0L-43 -14"/>
    </g>
    <polygon points="0,-36 30,-10 14,20 -22,30 -34,-11" fill="rgba(234,10,142,.3)" stroke="var(--pink)" stroke-width="1.2"/>
  </svg>
</section>
<section class="slide" style="left:275px;top:1035px;width:232px;height:130px">
  <svg width="232" height="130" style="position:absolute;left:0;top:0">
    <path d="M0 95 Q80 70 140 130 L0 130Z" fill="var(--grey-pale)"/>
    <path d="M0 95 Q80 70 140 130" fill="none" stroke="var(--pink)" stroke-width="1.5"/>
    <path d="M232 0 L232 60 Q180 30 160 0Z" fill="var(--grey-pale)"/>
  </svg>
  <div style="position:absolute;left:0;right:0;top:52px;text-align:center;font-weight:800;font-size:14px;color:var(--ink)">Any Questions?</div>
  <div style="position:absolute;left:107px;top:74px;width:18px;height:2px;background:var(--pink)"></div>
</section>
<section class="slide dark" style="left:519px;top:1035px;width:232px;height:130px">
  <svg width="232" height="130" style="position:absolute;left:0;top:0">
    <path d="M0 130 Q60 80 232 100 L232 130Z" fill="#2a2a2a"/>
    <path d="M0 130 Q60 80 232 100" fill="none" stroke="var(--pink)" stroke-width="1.5"/>
  </svg>
  <div style="position:absolute;left:0;right:0;top:52px;text-align:center;font-weight:800;font-size:14px;color:#fff">THANK YOU</div>
</section>

</body>
</html>
```